| 学生向け就職活動情報サイトのバナーを募集します。内容は同じですが3種類のサイズが必要なため、1種類のみ作成して応募していただき、こちらで選定した方に残り2種類の画像も依頼致します。 <バナー内の文言> 就活エントリー締切カレンダー <サイズ> (1)内部リンク用バナー 300×100 (2)ページ内画像 1200*800 (3)SNS用画像 1200*630 以上3種類 まずは(1)のみ作成してご応募ください。こちらで選定した方に残り2種類の画像も依頼させていただきます。 ※3種類の画像を納品していただいた時点で契約金額をお支払いします。 <画像のイメージ> 添付ファイルに参考画像を載せましたので、画像の雰囲気の参考にしてください。 (1)の内部リンク用バナーにつきましては、「banner」フォルダ内の4枚の画像と共に縦に並べることになります。 サイズや内容は関係ありません。 ご応募お待ちしております。 |
もっともイメージに合っていましたので採用させていただきました。
みなさまご提案ありがとうございました。

```html
<!DOCTYPE html>
<html lang="ja">
<head>
<meta charset="utf-8">
<title>就活エントリー締切カレンダー</title>
<link rel="stylesheet" href="https://fonts.googleapis.com/css2?family=M+PLUS+Rounded+1c:wght@900&display=swap">
<style>
  :root {
    --bg: #ffffff;
    --c1: #f7a800;
    --c2: #8cc63f;
    --c3: #22a93c;
    --c4: #1e8fd6;
    --c5: #1d2f8c;
    --c6: #7b2b93;
    --c7: #b1288f;
    --c8: #e8428f;
    --c9: #ec4a2a;
    --c0: #e1211b;
  }
  * { margin: 0; padding: 0; box-sizing: border-box; }
  html, body { width: 1200px; height: 400px; overflow: hidden; background: var(--bg); }
  .banner { position: relative; width: 1200px; height: 400px; overflow: hidden; background: var(--bg); }

  .number-row { position: absolute; height: 90px; }
  .number-row--upper {
    left: 14px; top: 12px; width: 652px;
    background: linear-gradient(90deg, var(--c1), var(--c2), var(--c3), var(--c4), var(--c5));
  }
  .number-row--lower {
    left: 506px; top: 290px; width: 626px;
    background: linear-gradient(90deg, var(--c6), var(--c7), var(--c8), var(--c9), var(--c0));
  }

  .stripes { position: absolute; inset: 0; }

  .banner__title {
    position: absolute; left: 0; right: 0; top: 148px;
    text-align: center;
    font-family: "M PLUS Rounded 1c", sans-serif; font-weight: 900;
    font-size: 78px; line-height: 1;
    white-space: nowrap;
  }
  .t1 { color: #f39800; } .t2 { color: #f2b200; } .t3 { color: #8cc63f; }
  .t4 { color: #22a93c; } .t5 { color: #13a5a0; } .t6 { color: #1e8fd6; }
  .t7 { color: #2a5fb8; } .t8 { color: #5a3a9e; } .t9 { color: #7b2b93; }
  .t10 { color: #b1288f; } .t11 { color: #e8428f; } .t12 { color: #ec4a5a; }
  .t13 { color: #ec4a2a; } .t14 { color: #e1211b; }
</style>
</head>
<body>
<div class="banner">
  <svg class="stripes" viewBox="0 0 1200 400" width="1200" height="400" aria-hidden="true">
    <polygon points="0,0 40,0 0,40" fill="var(--c1)"/>
    <polygon points="1200,400 1160,400 1200,360" fill="var(--c0)"/>
    <g stroke-width="3">
      <line x1="710" y1="24" x2="1180" y2="24" stroke="var(--c1)"/>
      <line x1="710" y1="40" x2="1080" y2="40" stroke="var(--c2)"/>
      <line x1="710" y1="58" x2="1020" y2="58" stroke="var(--c3)"/>
      <line x1="710" y1="76" x2="940" y2="76" stroke="var(--c4)"/>
      <line x1="710" y1="92" x2="900" y2="92" stroke="var(--c5)"/>
      <line x1="20" y1="300" x2="490" y2="300" stroke="var(--c6)"/>
      <line x1="120" y1="318" x2="490" y2="318" stroke="var(--c7)"/>
      <line x1="180" y1="336" x2="490" y2="336" stroke="var(--c8)"/>
      <line x1="260" y1="354" x2="490" y2="354" stroke="var(--c9)"/>
      <line x1="300" y1="370" x2="490" y2="370" stroke="var(--c0)"/>
    </g>
  </svg>

  <div class="number-row number-row--upper" role="img" aria-label="数字1から5の立体ブロックのイラスト"></div>
  <div class="number-row number-row--lower" role="img" aria-label="数字6から0の立体ブロックのイラスト"></div>

  <h1 class="banner__title"><span class="t1">就</span><span class="t2">活</span><span class="t3">エ</span><span class="t4">ン</span><span class="t5">ト</span><span class="t6">リ</span><span class="t7">ー</span><span class="t8">締</span><span class="t9">切</span><span class="t10">カ</span><span class="t11">レ</span><span class="t12">ン</span><span class="t13">ダ</span><span class="t14">ー</span></h1>
</div>
</body>
</html>
```